We are a music event management company based out of Syracuse, NY but we do business in multiple areas like the mid-west and Florida.

Our primary events revolve around the Electronic Dance Music scene. (acts like Brightmoor, Coastal Pulse Syndicate, Dorian Falk)

We would like a clean cut business card with Voltarine written on the back. In Voltarine we would like the u to be shaped like a sixteenth note. The colors green and silver would be nice to see somehow but not necessary. Feel free to play around with it and have fun because that's what our business is about, Having Fun!

Some similar examples for reference would be the Neon Orchard or Glowing Tulip Jubilee website.

Our goal is to provide people with an experience, not just a concert. There is a difference.

```html
<!DOCTYPE html>
<html lang="en">
<head>
<meta charset="utf-8">
<title>Voltarine — Business Card</title>
<link rel="stylesheet" href="https://fonts.googleapis.com/css2?family=Orbitron:wght@900&display=swap">
<style>
  :root {
    --page-bg: #ffffff;
    --card-black: #050505;
    --card-charcoal: #232323;
    --sheen-grey: #6a6a6a;
    --ribbon-grey: #4a4a4a;
    --hex-dark: #151515;
    --hex-light: #2e2e2e;
    --volt-blue-deep: #0a72dc;
    --volt-blue: #1a90ff;
    --volt-blue-light: #bfe0ff;
    --silver: #d6d8da;
  }
  html, body {
    margin: 0;
    padding: 0;
    width: 1200px;
    height: 1000px;
    overflow: hidden;
    background: var(--page-bg);
  }
  .canvas {
    position: relative;
    width: 1200px;
    height: 1000px;
  }
  .business-card {
    position: absolute;
    left: 0;
    top: 0;
    width: 1200px;
    height: 1000px;
  }
  .wordmark {
    font-family: "Orbitron", "Arial Black", sans-serif;
    font-weight: 900;
    font-size: 60px;
    fill: var(--silver);
  }
</style>
</head>
<body>
<main class="canvas">
  <svg class="business-card" viewBox="0 0 1200 1000" width="1200" height="1000" aria-label="Voltarine business card">
    <defs>
      <clipPath id="card-shape">
        <rect x="127" y="229" width="946" height="541" rx="36" ry="36"/>
      </clipPath>
      <linearGradient id="card-body" x1="0" y1="0" x2="1" y2="0">
        <stop offset="0" stop-color="var(--card-black)"/>
        <stop offset="0.42" stop-color="var(--card-charcoal)"/>
        <stop offset="0.55" stop-color="var(--sheen-grey)"/>
        <stop offset="0.62" stop-color="var(--card-charcoal)"/>
        <stop offset="0.85" stop-color="#2a2a2a"/>
        <stop offset="1" stop-color="var(--card-black)"/>
      </linearGradient>
      <linearGradient id="hex-field" x1="0" y1="0" x2="1" y2="0">
        <stop offset="0" stop-color="var(--hex-dark)"/>
        <stop offset="0.6" stop-color="var(--hex-light)"/>
        <stop offset="1" stop-color="var(--hex-dark)"/>
      </linearGradient>
      <linearGradient id="band-blue" x1="127" y1="0" x2="1073" y2="0" gradientUnits="userSpaceOnUse">
        <stop offset="0" stop-color="var(--volt-blue-deep)"/>
        <stop offset="0.45" stop-color="var(--volt-blue)"/>
        <stop offset="0.53" stop-color="var(--volt-blue-light)"/>
        <stop offset="0.6" stop-color="var(--volt-blue)"/>
        <stop offset="1" stop-color="var(--volt-blue)"/>
      </linearGradient>
      <linearGradient id="ribbon-grey" x1="0" y1="0" x2="1" y2="0">
        <stop offset="0" stop-color="#1a1a1a"/>
        <stop offset="0.7" stop-color="var(--ribbon-grey)"/>
        <stop offset="1" stop-color="#2a2a2a"/>
      </linearGradient>
      <linearGradient id="facet-sheen" x1="0" y1="0" x2="1" y2="0">
        <stop offset="0" stop-color="#ffffff" stop-opacity="0.14"/>
        <stop offset="1" stop-color="#ffffff" stop-opacity="0"/>
      </linearGradient>
    </defs>

    <g class="card" clip-path="url(#card-shape)">
      <rect class="card-body" x="127" y="229" width="946" height="541" fill="url(#card-body)"/>

      <rect class="texture-top" x="127" y="229" width="700" height="110" fill="url(#hex-field)" role="img" aria-label="Dark hexagon texture pattern"/>
      <rect class="texture-bottom" x="127" y="660" width="700" height="110" fill="url(#hex-field)" role="img" aria-label="Dark hexagon texture pattern"/>

      <path class="ribbon ribbon-top" d="M127,317 H590 C680,317 720,290 790,229 H830 C740,300 700,337 600,337 H127 Z" fill="url(#ribbon-grey)"/>
      <path class="ribbon ribbon-bottom" d="M127,682 H590 C680,682 720,709 790,770 H830 C740,699 700,662 600,662 H127 Z" fill="url(#ribbon-grey)"/>

      <path class="band band-top" d="M127,337 H600 C700,337 730,300 810,229 H1073 V243 L785,355 C720,382 690,392 640,392 H127 Z" fill="url(#band-blue)"/>
      <path class="band band-bottom" d="M127,662 H600 C700,662 730,699 810,770 H1073 V756 L785,644 C720,617 690,607 640,607 H127 Z" fill="url(#band-blue)"/>

      <path class="facet" d="M828,229 H1073 V243 L785,355 L700,610 L620,392 Z" fill="url(#facet-sheen)"/>

      <text class="wordmark" x="268" y="523" textLength="646" lengthAdjust="spacing">VOLTARINE</text>
    </g>
  </svg>
</main>
</body>
</html>
```